Dental Lab Delivery Box Design 163x115x97mm

* AI file of the box attached
* Full-Color outside and one color inside
* Return pictures of the 3D design; so we can have a better idea of how it will turn out
* Match Logo Color and Design
* Please find attached Words doc for the wording
* Research the dental lab delivery
* Attached our sister lab dental lab design
*
Updates

Thank for designing! We are reviewing and asking designers for improvements. We have extended the due date! More designs welcome!

Target Market(s)

Dental Office

Industry/Entity Type

Dental Lab

Font styles to use
Serif

Colors
0054AA
0677BA
7BADD7
CADEEF
E8F1F8

Requirements
Must have
• Advance, Clean, and Matched Logo color
Nice to have
• Graphics
Should not have
• Too much words or over advertise

```html
<!DOCTYPE html>
<html lang="en">
<head>
<meta charset="utf-8">
<title>Veltra Dental Inc – Delivery Box Dieline</title>
<link rel="stylesheet" href="https://fonts.googleapis.com/css2?family=Aleo:wght@400&family=Montserrat:wght@400;600&display=swap">
<style>
  :root {
    --page: #ffffff;
    --box-blue: #55a9dc;
    --box-blue-light: #79c6f0;
    --panel-white: #ffffff;
    --brand-navy: #0054aa;
    --brand-mid: #0677ba;
    --cut: #c2187a;
    --score: #333a44;
    --label-grey: #c9ccd1;
    --ink: #1d1f22;
  }
  html, body {
    margin: 0;
    width: 1200px;
    height: 1200px;
    overflow: hidden;
    background: var(--page);
  }
  .dieline {
    display: block;
    margin-top: 32px;
    width: 1200px;
    height: 1136px;
  }
  .face-blue { fill: var(--box-blue); }
  .face-light { fill: var(--box-blue-light); }
  .face-white { fill: var(--panel-white); }
  .cut-line { fill: none; stroke: var(--cut); stroke-width: 1.2; }
  .score-line { fill: none; stroke: var(--score); stroke-width: 1; }
  .brand-name {
    font-family: "Montserrat", Arial, sans-serif;
    font-weight: 600;
    letter-spacing: 1px;
  }
  .brand-navy { fill: var(--brand-navy); }
  .brand-white { fill: #ffffff; }
  .label-word {
    font-family: "Montserrat", Arial, sans-serif;
    font-weight: 400;
    font-size: 40px;
    letter-spacing: 3px;
    fill: var(--label-grey);
  }
  .side-tagline {
    font-family: "Montserrat", Arial, sans-serif;
    font-size: 9px;
    fill: var(--brand-navy);
  }
  .welcome-copy {
    font-family: "Montserrat", Arial, sans-serif;
    font-size: 8.4px;
    fill: var(--brand-navy);
  }
  .headline-serif {
    font-family: "Aleo", Georgia, serif;
    font-size: 23px;
    fill: #ffffff;
  }
  .tagline-white {
    font-family: "Montserrat", Arial, sans-serif;
    font-size: 12.5px;
    fill: #ffffff;
  }
  .legend-text {
    font-family: "Montserrat", Arial, sans-serif;
    font-size: 14px;
    fill: var(--ink);
  }
</style>
</head>
<body>
<svg class="dieline" viewBox="0 0 1305 1235" xmlns="http://www.w3.org/2000/svg">
  <defs>
    <linearGradient id="lidArtGradient" x1="0" y1="0" x2="0" y2="1">
      <stop offset="0" stop-color="#cfe6f7"/>
      <stop offset="0.35" stop-color="#6fb4e6"/>
      <stop offset="1" stop-color="#2e86d0"/>
    </linearGradient>
    <radialGradient id="frontArtGradient" cx="0.75" cy="0.55" r="0.8">
      <stop offset="0" stop-color="#e9f4fc"/>
      <stop offset="0.3" stop-color="#3d95dc"/>
      <stop offset="0.7" stop-color="#0a64c0"/>
      <stop offset="1" stop-color="#5fb2ea"/>
    </radialGradient>
  </defs>

  <!-- Top dust flaps and top panel -->
  <g class="top-section">
    <rect class="face-blue" x="345" y="22" width="132" height="226"/>
    <rect class="face-blue" x="845" y="22" width="132" height="226"/>
    <rect class="face-white" x="477" y="40" width="368" height="208"/>
    <path class="cut-line" d="M477 41 H845 M359 41 H477 V248 M845 248 V41 H960 V222 L920 244 H845 M477 244 H400 L359 222 V41"/>
    <text class="brand-name brand-navy" x="661" y="146" font-size="20" text-anchor="middle">VELTRA DENTAL INC</text>
  </g>

  <!-- Middle band: sides, label panel, base, spine -->
  <g class="middle-band">
    <rect class="face-blue" x="24" y="249" width="223" height="254"/>
    <rect class="face-white" x="247" y="249" width="222" height="254"/>
    <rect class="face-blue" x="469" y="249" width="380" height="254"/>
    <rect class="face-white" x="849" y="249" width="51" height="254"/>
    <rect class="face-blue" x="900" y="249" width="26" height="254"/>
    <rect class="face-white" x="926" y="249" width="134" height="254"/>
    <rect class="face-blue" x="1060" y="249" width="235" height="254"/>
    <path class="cut-line" d="M247 256 H40 V322 L32 330 V426 L40 434 V496 H247 M1068 256 H1278 V322 L1286 330 V426 L1278 434 V496 H1068 M258 249 H1060 M258 503 H1060"/>
    <path class="score-line" d="M247 249 V503 M258 249 V503 M469 249 V503 M849 249 V503 M1060 249 V503 M1070 249 V503"/>
    <text class="label-word" transform="translate(384 378) rotate(-90)" text-anchor="middle">LABEL</text>
    <text class="brand-name brand-navy" font-size="11" transform="translate(303 428) rotate(-90)" text-anchor="middle">VELTRA DENTAL INC</text>
    <text class="brand-name brand-white" x="659" y="385" font-size="21" text-anchor="middle">VELTRA DENTAL INC</text>
    <text class="brand-name brand-navy" font-size="13" transform="translate(958 376) rotate(90)" text-anchor="middle">VELTRA DENTAL INC</text>
    <text class="side-tagline" transform="translate(910 376) rotate(90)" text-anchor="middle">Full Digital Dental Lab</text>
  </g>

  <!-- Inner lid panel with welcome copy -->
  <g class="inner-lid">
    <rect class="face-blue" x="339" y="505" width="136" height="208"/>
    <rect class="face-blue" x="845" y="507" width="129" height="206"/>
    <rect class="face-white" x="475" y="505" width="370" height="208"/>
    <path class="cut-line" d="M475 710 H358 V527 L398 507 H475 M845 710 H960 V532 L918 507 H845"/>
    <g transform="rotate(180 660 600)">
      <text class="brand-name brand-navy" x="660" y="655" font-size="17" text-anchor="middle">VELTRA DENTAL INC</text>
      <text class="welcome-copy" text-anchor="middle">
        <tspan x="660" y="516">Welcome to Veltra! Headquartered in Cedar Falls, Oregon,</tspan>
        <tspan x="660" y="529">we are a full digital dental lab for all you need. We strive to build</tspan>
        <tspan x="660" y="542">excellent relationships and services with our clients, utilize highly</tspan>
        <tspan x="660" y="555">experienced technicians and advanced case management systems.</tspan>
        <tspan x="660" y="568">Veltra stands for precision, care, trust and service. We care for your</tspan>
        <tspan x="660" y="581">team as one team. Veltra looks forward to building and improving</tspan>
        <tspan x="660" y="594">your reputation and bringing more smiles to our services.</tspan>
      </text>
    </g>
  </g>

  <!-- Outer lid panel -->
  <g class="outer-lid">
    <rect class="face-blue" x="260" y="715" width="800" height="257"/>
    <rect x="482" y="715" width="355" height="257" fill="url(#lidArtGradient)" role="img" aria-label="Soft blue wave and bokeh light background"/>
    <path class="cut-line" d="M482 716 L300 770 Q270 780 270 810 V880 Q270 912 300 922 L482 972 M837 716 L1020 770 Q1048 780 1048 810 V880 Q1048 912 1020 922 L837 972"/>
    <path class="score-line" d="M482 715 V972 M837 715 V972"/>
    <text class="headline-serif" x="661" y="925" text-anchor="middle">Every Detail Matters</text>
    <text class="tagline-white" x="661" y="946" text-anchor="middle">Full Digital Dental Lab</text>
  </g>

  <!-- Front panel -->
  <g class="front-panel">
    <rect class="face-light" x="251" y="978" width="817" height="213"/>
    <rect x="474" y="978" width="371" height="213" fill="url(#frontArtGradient)" role="img" aria-label="Glowing white molar tooth over flowing blue light waves"/>
    <path class="cut-line" d="M474 984 H305 Q282 986 280 1010 V1150 Q284 1178 312 1183 H474 M845 984 H1010 Q1042 988 1044 1030 V1120 Q1040 1176 1000 1183 H845"/>
    <path class="score-line" d="M474 978 V1191 M845 978 V1191"/>
    <text class="brand-name brand-white" x="595" y="1090" font-size="20" text-anchor="middle">VELTRA DENTAL INC</text>
    <text class="tagline-white" x="601" y="1136" text-anchor="middle">Full Digital Dental Lab</text>
  </g>

  <!-- Legend -->
  <g class="legend">
    <text class="legend-text" x="114" y="1108" text-anchor="middle">Cut Line</text>
    <line class="cut-line" x1="55" y1="1117" x2="172" y2="1117"/>
    <text class="legend-text" x="114" y="1143" text-anchor="middle">Score Line</text>
    <line class="score-line" x1="55" y1="1151" x2="172" y2="1151"/>
    <text class="legend-text" x="16" y="1194">Inner size:163x115x97mm</text>
  </g>
</svg>
</body>
</html>
```